Clikora - photography in NYC - leveraging big data and robotics

We've got a photography business in NYC. It is kind of on-demand photographers, but actually is just five of us who work as a team. Over the last three years we've taken tens of thousands of photographs and are now sitting on a load of great work. We want to leverage that in a way that lets people book either by event type or location. So, they would click on Harlow Green and a load of examples of our work would pop up. Or Wedding Shower, and relevant examples would pop up. We've got the pictures structured pretty well to enable this. Now we just need a website that illustrates this and then leads through the booking process (time, location, date, contact etc.) and payment.

Target Market(s)

Everyone - corporates, real estate, tourists, families, headshots, bloggers, products, wedding showers, baby showers, engagements, venues, restaurants/bars, holiday pictures, City Hall weddings, kids birthday parties, adult birthday parties, PR companies, corporate events.... long list.

Industry/Entity Type

Photographer

Number of Pages Required

5+ page

Colors

Designer to choose colors to be used in the design.

Requirements
Must have
• A great, engaging landing page which people can choose by event type or location. This would then pull in examples of our work in that location or in that event type. Then they go through the booking process. This is simple capturing key details - see here https://clikora.example/book/
Nice to have
• Social links
Should not have
• Nothing specific.

```html
<!DOCTYPE html>
<html lang="en">
<head>
<meta charset="utf-8">
<title>Clikora — Book a Photographer</title>
<link rel="stylesheet" href="https://fonts.googleapis.com/css2?family=Saira:wght@400;500;600;700&display=swap">
<style>
  :root {
    --sun: #f8c31c;
    --coral: #ee5253;
    --ink: #333333;
    --field: #fdf0c4;
    --button: #f07b6e;
    --bubble: #2a7bd1;
    --ring: #e9a80f;
    --studio-light: #d9dadb;
    --studio-blue: #2e6fc4;
    --white: #ffffff;
  }
  * { margin: 0; padding: 0; box-sizing: border-box; }
  html, body { width: 1200px; height: 598px; overflow: hidden; }
  body {
    background: var(--sun);
    font-family: "Saira", "Arial", sans-serif;
    color: var(--ink);
    position: relative;
  }
  .brand {
    position: absolute; left: 112px; top: 2px;
    font-size: 70px; font-weight: 700; letter-spacing: 1px;
    color: var(--coral); line-height: 1; text-transform: uppercase;
  }
  .help {
    position: absolute; left: 886px; top: 24px;
    display: flex; align-items: center; gap: 8px;
  }
  .help-icon { width: 27px; height: 27px; }
  .help-label { font-size: 14px; font-weight: 500; color: var(--coral); line-height: 1.05; }
  .help-number { font-size: 20px; font-weight: 700; color: var(--ink); line-height: 1; letter-spacing: 0.5px; }
  .hero {
    position: absolute; left: 112px; top: 222px;
  }
  .hero-title {
    font-size: 37px; font-weight: 600; line-height: 54px; color: var(--ink);
    letter-spacing: 0.3px;
  }
  .hero-bubble {
    position: absolute; left: 328px; top: 17px; width: 76px; height: 76px;
  }
  .event-form {
    display: flex; margin-top: 19px; width: 398px; height: 45px;
  }
  .event-input {
    flex: 1; border: 0; background: var(--field);
    font-family: "Arial", sans-serif; font-size: 15px; color: var(--ink);
    padding: 0 8px;
  }
  .event-input::placeholder { color: var(--ink); }
  .event-next {
    width: 76px; border: 0; background: var(--button); color: var(--white);
    font-family: "Saira", "Arial", sans-serif; font-size: 21px; font-weight: 500;
  }
  .studio {
    position: absolute; left: 688px; top: 120px;
    width: 428px; height: 428px; border-radius: 50%;
    border: 7px solid var(--ring);
    background: radial-gradient(circle at 50% 45%, var(--studio-light) 0%, #a9b0b4 55%, var(--studio-blue) 100%);
  }
  .copyright {
    position: absolute; left: 113px; top: 563px;
    font-size: 13px; font-weight: 600; color: var(--ink); letter-spacing: 0.3px;
  }
</style>
</head>
<body>
  <header>
    <div class="brand">Clikora</div>
    <div class="help">
      <svg class="help-icon" viewBox="0 0 28 28" aria-hidden="true">
        <circle cx="14" cy="14" r="12.5" fill="none" stroke="#333" stroke-width="1.6"/>
        <path d="M10.5 7.5c-1.5.6-2.2 2-1.8 3.6.9 3.4 3.4 6.6 6.2 8.5 1.3.9 2.9.6 3.8-.6l.6-.8-2.6-2.2-1.3 1.1c-1.6-1-3-2.8-3.6-4.6l1.4-.9-1.2-3.2z" fill="#333"/>
      </svg>
      <div>
        <div class="help-label">Need Help Call Us Today</div>
        <div class="help-number">555.014.2290</div>
      </div>
    </div>
  </header>

  <main class="hero">
    <h1 class="hero-title">What Do You<br>Want Pictures of</h1>
    <svg class="hero-bubble" viewBox="0 0 76 76" aria-hidden="true">
      <path d="M40 2a36 36 0 1 1-17 68l-18 4 6-14A36 36 0 0 1 40 2z" fill="var(--bubble)"/>
      <path d="M31 30c0-6 4-10 10-10s10 4 10 9c0 7-8 7-8 14h-6c0-9 8-9 8-14 0-2-2-4-4-4s-4 2-4 5z" fill="var(--sun)"/>
      <rect x="37" y="47" width="6" height="7" fill="var(--sun)"/>
    </svg>
    <form class="event-form">
      <input class="event-input" type="text" placeholder="Enter Your Event Name">
      <button class="event-next" type="button">Next</button>
    </form>
  </main>

  <div class="studio" role="img" aria-label="Illustration of a bearded photographer holding a camera in a studio with lights"></div>

  <footer class="copyright">Copyright © 2018 Clikora. All Rights Reserved.</footer>
</body>
</html>
```